Home Page Design (PSD Only) - Ecommerce - Yarn, Apparel and Socks

We need a new home page design for our e-commerce site FernMeadow.com.
Our team will create the HTML/CSS using the Bootstrap framework. We just need the final PSD and slices. Our brand/logo will remain however our focus has shifted to two key product categories. 1: Yarn 2: Socks. We also sell products in the other categories but these will not be the focus and jewelry will likely go away.

Our socks and yarn are focused on "Affordable Luxury" We carry over 2000 yarns (Huge Selection) and have the largest selection on the internet for Alpaca Socks.

Our buyers are very different. Most yarn buyers are women 25-55 who are very tactile. They want to feel the yarn so this somehow needs to come through. Clean and Warm, Affordable Luxury.

Our sock buyers buy premium socks ($15-20/pair) are split male/female and have little interest in Yarn or Knitting. I realize we should likely have 2 different sites but we've spent 7 years building the brand and have loyalty from both markets and are not getting x-sell. Especially knitters who buy our socks and stuffed bears, etc for gifts.

We'll be moving toward a new responsive design based on the Bootstrap framework under the hood.
Updates

Target Market(s)

Women for the Yarn (knitters). Split 60F/40M for socks
Current site is blue. Feel free to update the colors to make the site more attractive for women.

Industry/Entity Type

E-Commerce

Requirements
Must have
• Rotating Hero, Global Search, Must incorporate our blue logo (or inverse). Social bar for Chirply, Pagebook, Clipwall, Loopsy (yarn social site), Purlnotes (yarn social site).
Can use warm colors to appeal more to women.
Must support a responsive design (bootstrap)
Nice to have
• Site should resonate with Knitters but not alienate users who just come to shop for Socks, Stuffed Bears, Sweaters, etc.
Clean, simple design, but with warmth and upscale feeling.
Yarn sites: skeinhub.com, loomtrove.com
Sock/Apparel Sites: toastytoes.com, heelworksco.com, birchvale.com, lum.com

I've added some initial comps that tested OK but early feedback was it was too plain and lacked emotional appeal.

```html
<!DOCTYPE html>
<html lang="en">
<head>
<meta charset="utf-8">
<title>FernMeadow – Home</title>
<link rel="stylesheet" href="https://fonts.googleapis.com/css2?family=Arimo:ital,wght@0,400;0,700;1,400&family=Rokkitt:wght@400;600&family=Rambla:wght@400;700&family=Oswald:wght@400&display=swap">
<style>
:root{
  --blue:#1a7cc2;
  --blue-dark:#1565a6;
  --ink:#333;
  --muted:#555;
  --paper:#f2f2f2;
  --paper-2:#ececec;
  --nav-top:#4a4a4a;
  --nav-bot:#262626;
  --footer:#2d2d2d;
  --footer-base:#232323;
  --footer-text:#8a8a8a;
  --plum:#7b2e6c;
  --star:#f39a1e;
}
*{box-sizing:border-box;margin:0;padding:0}
html,body{width:1071px;height:1200px;overflow:hidden;background:var(--paper)}
body{font-family:Arimo,Arial,sans-serif;color:var(--ink)}
.page{position:absolute;left:0;top:0;width:1200px;height:1344px;transform:scale(.8925);transform-origin:0 0;background:var(--paper)}
.abs{position:absolute}

/* header */
.site-header{position:absolute;left:0;top:0;width:1200px;height:174px;background:linear-gradient(#f5f5f5,#ececec)}
.zigzag-top{position:absolute;left:0;top:0;width:1200px;height:8px}
.brand{position:absolute;left:97px;top:62px;font-family:Arimo,Arial,sans-serif;font-weight:700;font-size:44px;color:var(--blue);display:flex;align-items:center;gap:12px;letter-spacing:.5px}
.brand-dot{width:18px;height:18px;border-radius:50%;background:var(--blue)}
.account-links{position:absolute;left:965px;top:22px;font-size:13px;font-weight:700;color:var(--blue);letter-spacing:.3px}
.search-label{position:absolute;left:799px;top:126px;font-size:12px;font-weight:700;letter-spacing:1px;color:#333}
.search-box{position:absolute;left:865px;top:119px;width:233px;height:29px;border-radius:15px;background:#e4e4e4;border:1px solid #d2d2d2;box-shadow:inset 0 1px 2px rgba(0,0,0,.1);font-size:12px;color:#444;padding:7px 0 0 27px}
.search-box svg{position:absolute;right:12px;top:6px}

/* nav */
.main-nav{position:absolute;left:0;top:174px;width:1200px;height:47px;background:linear-gradient(var(--nav-top),var(--nav-bot));display:flex;padding-left:113px}
.main-nav a{display:block;height:47px;line-height:44px;color:#fff;font-size:15px;text-decoration:none;padding:0 27px;border-right:1px solid #1c1c1c;box-shadow:1px 0 0 #555}
.main-nav a:last-child{border:none;box-shadow:none}
.main-nav a.active{background:#1f1f1f;border:1px solid #111;border-radius:3px;height:35px;line-height:33px;margin-top:6px;padding:0 22px;box-shadow:inset 0 1px 3px rgba(0,0,0,.6),0 1px 0 #555;margin-right:0}

/* hero */
.hero{position:absolute;left:0;top:221px;width:1200px;height:459px;background:#f3f3f3;overflow:hidden}
.hero-photo{position:absolute;left:560px;top:0;width:640px;height:459px;background:linear-gradient(100deg,rgba(243,243,243,1) 0%,rgba(236,238,236,.9) 18%,#dfe6e2 40%,#c8d4cf 60%,#a9c0bb 78%,#d8cbbd 100%)}
.hero-title{position:absolute;left:110px;top:58px;font-family:Rokkitt,serif;line-height:50px}
.hero-title .accent{color:var(--blue);font-size:54px;font-weight:600;display:block}
.hero-title .main{color:#2a2a2a;font-size:54px;font-weight:400;display:block;letter-spacing:1px}
.hero-copy{position:absolute;left:108px;top:174px;width:360px;font-size:12.5px;line-height:21px;color:#444}
.hero-links{position:absolute;top:230px;list-style:none;font-size:12.5px;color:#333}
.hero-links li{height:24px;padding-left:14px;position:relative}
.hero-links li::before{content:"";position:absolute;left:2px;top:4px;border-left:4px solid var(--blue);border-top:4px solid transparent;border-bottom:4px solid transparent}
.btn-primary{position:absolute;left:108px;top:378px;width:103px;height:37px;border-radius:3px;background:linear-gradient(#2d8fd6,var(--blue-dark));color:#fff;font-size:11px;font-weight:700;text-align:center;line-height:37px;box-shadow:0 1px 2px rgba(0,0,0,.3)}
.zigzag-bottom{position:absolute;left:0;top:664px;width:1200px;height:20px}

/* product cards */
.promo{position:absolute;top:728px;width:312px;height:159px;background:linear-gradient(#fafafa,#fff);border:1px solid #dcdcdc;border-radius:6px;box-shadow:0 6px 8px -6px rgba(0,0,0,.25)}
.promo h2{position:absolute;left:12px;top:12px;font-family:Rambla,sans-serif;font-weight:700;font-size:20px;color:#2f2f2f;letter-spacing:.3px}
.promo .thumb{position:absolute;left:14px;top:50px;width:97px;height:97px;background:#fff;border:1px solid #e0e0e0;box-shadow:0 1px 3px rgba(0,0,0,.15);padding:6px}
.promo .thumb div{width:100%;height:100%}
.promo .name{position:absolute;left:144px;top:50px;font-size:12.5px;font-weight:700;color:#555;line-height:18px}
.promo .stars{position:absolute;left:144px;top:92px;display:flex;gap:1px}
.promo .price{position:absolute;left:147px;top:128px;font-size:18px;font-style:italic;font-weight:700;color:#333}
.promo .details{position:absolute;right:15px;top:130px;font-size:12.5px;font-style:italic;color:#444;text-decoration:underline}

/* blog */
.post{position:absolute;top:968px}
.post .thumb{position:absolute;left:0;top:0;width:117px;height:117px;background:#fff;border:1px solid #ddd;padding:4px;box-shadow:0 1px 2px rgba(0,0,0,.1)}
.post .thumb div{width:100%;height:100%}
.post h3{position:absolute;left:127px;top:0;white-space:nowrap;font-size:15px;font-weight:700;color:#333;letter-spacing:.3px;display:flex;align-items:center;gap:9px}
.post p{position:absolute;left:127px;top:24px;font-size:12px;line-height:19px;color:#444}
.post .more{position:absolute;left:127px;font-family:Oswald,sans-serif;font-size:14px;color:var(--plum);letter-spacing:-.2px}
.post-divider{position:absolute;left:588px;top:965px;width:3px;height:140px;background:linear-gradient(rgba(0,0,0,0),rgba(0,0,0,.12),rgba(0,0,0,0))}

/* footer */
.info-bar{position:absolute;left:0;top:1149px;width:1200px;height:36px;background:var(--blue);color:#fff;font-size:12.5px;font-weight:700;padding:10px 0 0 112px}
.site-footer{position:absolute;left:0;top:1185px;width:1200px;height:111px;background:var(--footer)}
.footer-col{position:absolute;top:30px;font-size:11.5px;color:var(--footer-text);line-height:19px;letter-spacing:.5px}
.footer-col h4{font-size:12px;font-weight:700;color:#9a9a9a;margin-bottom:2px}
.footer-brand{position:absolute;left:823px;top:48px;font-size:44px;font-weight:700;color:#555;display:flex;align-items:center;gap:12px}
.footer-brand span{width:18px;height:18px;border-radius:50%;background:#555}
.footer-base{position:absolute;left:0;top:1296px;width:1200px;height:48px;background:var(--footer-base)}
.social{position:absolute;left:107px;top:13px;display:flex;gap:14px;align-items:center}
.social a{display:flex;align-items:center;gap:4px;font-size:10px;color:#aaa;text-decoration:none}
.social i{display:block;width:22px;height:22px;border-radius:2px}
.copyright{position:absolute;left:838px;top:14px;font-size:11px;color:#999}
</style>
</head>
<body>
<div class="page">

  <header class="site-header">
    <svg class="zigzag-top" viewBox="0 0 1200 8" preserveAspectRatio="none"><path fill="#3a3a3a" d="M0 0H1200V2 L1194 8 1188 2 1182 8 1176 2 1170 8 1164 2 1158 8 1152 2 1146 8 1140 2 1134 8 1128 2 1122 8 1116 2 1110 8 1104 2 1098 8 1092 2 1086 8 1080 2 1074 8 1068 2 1062 8 1056 2 1050 8 1044 2 1038 8 1032 2 1026 8 1020 2 1014 8 1008 2 1002 8 996 2 990 8 984 2 978 8 972 2 966 8 960 2 954 8 948 2 942 8 936 2 930 8 924 2 918 8 912 2 906 8 900 2 894 8 888 2 882 8 876 2 870 8 864 2 858 8 852 2 846 8 840 2 834 8 828 2 822 8 816 2 810 8 804 2 798 8 792 2 786 8 780 2 774 8 768 2 762 8 756 2 750 8 744 2 738 8 732 2 726 8 720 2 714 8 708 2 702 8 696 2 690 8 684 2 678 8 672 2 666 8 660 2 654 8 648 2 642 8 636 2 630 8 624 2 618 8 612 2 606 8 600 2 594 8 588 2 582 8 576 2 570 8 564 2 558 8 552 2 546 8 540 2 534 8 528 2 522 8 516 2 510 8 504 2 498 8 492 2 486 8 480 2 474 8 468 2 462 8 456 2 450 8 444 2 438 8 432 2 426 8 420 2 414 8 408 2 402 8 396 2 390 8 384 2 378 8 372 2 366 8 360 2 354 8 348 2 342 8 336 2 330 8 324 2 318 8 312 2 306 8 300 2 294 8 288 2 282 8 276 2 270 8 264 2 258 8 252 2 246 8 240 2 234 8 228 2 222 8 216 2 210 8 204 2 198 8 192 2 186 8 180 2 174 8 168 2 162 8 156 2 150 8 144 2 138 8 132 2 126 8 120 2 114 8 108 2 102 8 96 2 90 8 84 2 78 8 72 2 66 8 60 2 54 8 48 2 42 8 36 2 30 8 24 2 18 8 12 2 6 8 0 2Z"/></svg>
    <div class="brand">FernMeadow<span class="brand-dot"></span></div>
    <div class="account-links">LOGIN &nbsp;|&nbsp; REGISTER</div>
    <div class="search-label">SEARCH</div>
    <div class="search-box">Find patterns or yarn
      <svg width="16" height="16" viewBox="0 0 16 16"><circle cx="6" cy="6" r="4.5" fill="none" stroke="#1a7cc2" stroke-width="2"/><path d="M9.5 9.5 14 14" stroke="#1a7cc2" stroke-width="2.5" stroke-linecap="round"/></svg>
    </div>
  </header>

  <nav class="main-nav">
    <a class="active">Welcome</a><a>Women</a><a>men</a><a>Kids</a><a>Home Goods</a><a>Jwelry</a><a>Yarn &amp; Fiber</a><a>Gift</a><a>Clearance</a>
  </nav>

  <section class="hero">
    <div class="hero-photo" role="img" aria-label="Photo of a smiling woman in a white blouse wearing a teal knitted lace scarf, seated in a bright sunroom"></div>
    <h1 class="hero-title"><span class="accent">Yarn Sale</span><span class="main">At Least 30% Off</span></h1>
    <p class="hero-copy">We make it easy to find your favorite yarn brands and yarn colors for your knitting projects at discount yarn prices.</p>
    <ul class="hero-links" style="left:108px"><li>&nbsp;Alpaca vs Cashmere</li><li>Care instructions</li><li>Happy Customers</li><li>Read our Blog</li><li>Alpacas For Sale</li></ul>
    <ul class="hero-links" style="left:292px"><li>Alpaca vs Cashmere</li><li>Care instructions</li><li>Happy Customers</li><li>Read our Blog</li><li>Alpacas For Sale</li></ul>
    <div class="btn-primary">Read More</div>
  </section>
  <svg class="zigzag-bottom" viewBox="0 0 1200 20" preserveAspectRatio="none"><path fill="#f2f2f2" d="M0 20V8 L5 3 10 8 15 3 20 8 25 3 30 8 35 3 40 8 45 3 50 8 55 3 60 8 65 3 70 8 75 3 80 8 85 3 90 8 95 3 100 8 105 3 110 8 115 3 120 8 125 3 130 8 135 3 140 8 145 3 150 8 155 3 160 8 165 3 170 8 175 3 180 8 185 3 190 8 195 3 200 8 205 3 210 8 215 3 220 8 225 3 230 8 235 3 240 8 245 3 250 8 255 3 260 8 265 3 270 8 275 3 280 8 285 3 290 8 295 3 300 8 305 3 310 8 315 3 320 8 325 3 330 8 335 3 340 8 345 3 350 8 355 3 360 8 365 3 370 8 375 3 380 8 385 3 390 8 395 3 400 8 405 3 410 8 415 3 420 8 425 3 430 8 435 3 440 8 445 3 450 8 455 3 460 8 465 3 470 8 475 3 480 8 485 3 490 8 495 3 500 8 505 3 510 8 515 3 520 8 525 3 530 8 535 3 540 8 545 3 550 8 555 3 560 8 565 3 570 8 575 3 580 8 585 3 590 8 595 3 600 8 605 3 610 8 615 3 620 8 625 3 630 8 635 3 640 8 645 3 650 8 655 3 660 8 665 3 670 8 675 3 680 8 685 3 690 8 695 3 700 8 705 3 710 8 715 3 720 8 725 3 730 8 735 3 740 8 745 3 750 8 755 3 760 8 765 3 770 8 775 3 780 8 785 3 790 8 795 3 800 8 805 3 810 8 815 3 820 8 825 3 830 8 835 3 840 8 845 3 850 8 855 3 860 8 865 3 870 8 875 3 880 8 885 3 890 8 895 3 900 8 905 3 910 8 915 3 920 8 925 3 930 8 935 3 940 8 945 3 950 8 955 3 960 8 965 3 970 8 975 3 980 8 985 3 990 8 995 3 1000 8 1005 3 1010 8 1015 3 1020 8 1025 3 1030 8 1035 3 1040 8 1045 3 1050 8 1055 3 1060 8 1065 3 1070 8 1075 3 1080 8 1085 3 1090 8 1095 3 1100 8 1105 3 1110 8 1115 3 1120 8 1125 3 1130 8 1135 3 1140 8 1145 3 1150 8 1155 3 1160 8 1165 3 1170 8 1175 3 1180 8 1185 3 1190 8 1195 3 1200 8V20Z"/></svg>

  <article class="promo" style="left:111px">
    <h2>TOOL SALE</h2>
    <div class="thumb"><div role="img" aria-label="Photo of a skein of turquoise yarn" style="background:linear-gradient(135deg,#2bb3c8,#1690a8)"></div></div>
    <div class="name">Harlow 9 Glove &amp; Ball<br>Combo Trees and Birds</div>
    <div class="stars"><svg width="86" height="16" viewBox="0 0 86 16"><g fill="#f39a1e"><rect x="0" width="16" height="16"/><rect x="17" width="16" height="16"/><rect x="34" width="16" height="16"/><rect x="51" width="16" height="16"/></g><rect x="68" width="16" height="16" fill="#ddd"/><g fill="#fff"><path id="s" d="M8 2.5 9.6 6.2 13.5 6.5 10.5 9 11.5 13 8 10.8 4.5 13 5.5 9 2.5 6.5 6.4 6.2Z"/><use href="#s" x="17"/><use href="#s" x="34"/><use href="#s" x="51"/><use href="#s" x="68"/></g></svg></div>
    <div class="price">$8.00</div>
    <div class="details">Details</div>
  </article>
  <article class="promo" style="left:449px">
    <h2 style="left:27px">40% OFF CROCHET HOOKS</h2>
    <div class="thumb" style="left:17px"><div role="img" aria-label="Photo of blue and lime green yarn balls" style="background:linear-gradient(120deg,#9fc3dc,#6a9fc7 55%,#a8c53a)"></div></div>
    <div class="name">Harlow 9 Glove &amp; Ball<br>Combo Trees and Birds</div>
    <div class="stars"><svg width="86" height="16" viewBox="0 0 86 16"><g fill="#f39a1e"><rect x="0" width="16" height="16"/><rect x="17" width="16" height="16"/><rect x="34" width="16" height="16"/><rect x="51" width="16" height="16"/></g><rect x="68" width="16" height="16" fill="#ddd"/><g fill="#fff"><use href="#s"/><use href="#s" x="17"/><use href="#s" x="34"/><use href="#s" x="51"/><use href="#s" x="68"/></g></svg></div>
    <div class="price">$28.00</div>
    <div class="details">Details</div>
  </article>
  <article class="promo" style="left:786px">
    <h2 style="left:24px">NEW ARIVALS</h2>
    <div class="thumb" style="left:25px;width:92px"><div role="img" aria-label="Photo of red yarn balls on white" style="background:radial-gradient(circle at 50% 55%,#d8242a 0,#c81d22 35%,#f4f4f4 60%)"></div></div>
    <div class="name" style="left:139px">Harlow 9 Glove &amp; Ball<br>Combo Trees and Birds</div>
    <div class="stars" style="left:139px"><svg width="86" height="16" viewBox="0 0 86 16"><g fill="#f39a1e"><rect x="0" width="16" height="16"/><rect x="17" width="16" height="16"/><rect x="34" width="16" height="16"/><rect x="51" width="16" height="16"/></g><rect x="68" width="16" height="16" fill="#ddd"/><g fill="#fff"><use href="#s"/><use href="#s" x="17"/><use href="#s" x="34"/><use href="#s" x="51"/><use href="#s" x="68"/></g></svg></div>
    <div class="price" style="left:142px">$68.00</div>
    <div class="details">Details</div>
  </article>

  <article class="post" style="left:108px;width:460px">
    <div class="thumb"><div role="img" aria-label="Photo of hands wearing teal cabled fingerless gloves" style="background:linear-gradient(135deg,#3a8d9a,#5aa7b0 45%,#e6b79e 75%,#c98a6c)"></div></div>
    <h3><svg width="20" height="18" viewBox="0 0 20 18"><circle cx="3" cy="15" r="2.5" fill="#999"/><path d="M1 8a9 9 0 0 1 9 9M1 2a15 15 0 0 1 15 15" fill="none" stroke="#999" stroke-width="2.5"/></svg>WHITE CAPS FINGERLESS GLOVES</h3>
    <p>Marisol is my favorite yarn and Tidewater is hands down one<br>of my favorite blues so when I found a skein of it in my<br>stash I couldn't <b><i>wait</i></b> to make something with it!</p>
    <div class="more" style="top:86px">READ MORE</div>
  </article>
  <div class="post-divider"></div>
  <article class="post" style="left:633px;width:460px">
    <div class="thumb"><div role="img" aria-label="Photo of hands sewing the sleeve of a knitted sweater" style="background:linear-gradient(135deg,#4a3e46,#6c5a5e 45%,#8c7a74 70%,#5a4a50)"></div></div>
    <h3><svg width="20" height="18" viewBox="0 0 20 18"><rect x="1" y="2" width="18" height="11" rx="1" fill="none" stroke="#999" stroke-width="2"/><path d="M6 17h8M10 13v4" stroke="#999" stroke-width="2"/></svg>HOW TO SET IN SLEEVES</h3>
    <p>So you've just finished your knitted sweater – now what?<br>Now comes the fun part: you get to do the finishing! In the<br>first video, Maren shows you how to set in the sleeves of<br>your sweater.</p>
    <div class="more" style="top:106px">READ MORE</div>
  </article>

  <div class="info-bar">Order by Phone: 1-888-555-0147 &nbsp;|&nbsp;&nbsp; 100% Satisfaction Guaranteed!</div>

  <footer class="site-footer">
    <div class="footer-col" style="left:115px"><h4>Where's My Stuff?</h4>• Manage your Account<br>• Check your Order Status</div>
    <div class="footer-col" style="left:284px"><h4>Shipping &amp; Returns</h4>• View our Shipping Rates<br>• View our Returns Policy</div>
    <div class="footer-col" style="left:449px"><h4>Customer Support</h4>• Forgot your password?<br>• Visit Customer Service</div>
    <div class="footer-brand">FernMeadow<span></span></div>
  </footer>
  <div class="footer-base">
    <div class="social">
      <a><i style="background:#3b5998"></i>Pagebook</a>
      <a><i style="background:#2aa9e0"></i>Chirply</a>
      <a><i style="background:#f26522"></i>Postly</a>
      <a><i style="background:#1b75bb"></i>Linkwork</a>
      <a><i style="background:#3aa757"></i>Searchly</a>
    </div>
    <div class="copyright">© 2013 studioweave.ca| &nbsp;All right reserved</div>
  </div>

</div>
</body>
</html>
```